Labels/logo for luxury bath products

I am developing a range of luxury bath foams - aimed at the top end of the luxury market. My company name is VRE (very basic website can be seen at www.vremarket.example).

I am looking for a label design for the front of the bottle, which should incorporate the VRE logo as per the website (file attached), but embedded within a more intricate label design. I provide a link to a picture of the bottle below.

The bath foam will come in four fragrances: Vetiver, Sandalwood, Jasmine and Neroli. The label should include the fragrance name. So the label must include the brand name 'VRE' and the name of the fragrance - e.g. Sandalwood Bath Foam, Neroli Bath Foam, etc.

The products are aimed at both the male and female market and so shouldn't be too feminine.

A brand to take inspiration from is Mabel Fenwick: http://www.mabelfenwick.example/ - I like the labels that they use on their products, which is a gold embossed crest, which they use as the label for their products. I am not referring to their font, but to their label design - I like the embossed label, and am quite keen on metallics.

Conversely, I would like to add a contemporary edge to this design - I like the striping and contemporary fonts on this design: http://www.tamsin-gale.example/images/qbx41.jpg

My brand also harnesses the powers of natural flower ingredients, and so I am inspired by the products of Ylvane - ylvane.example. This labelling is more clinical and scientific.

Ideally I would like a label which combines these elements - i.e. a luxury label with a contemporary feel, that incorporate the scientific nature of the product.

The design needs to communicate high end luxury. The bottle is however apothecary style, and a nod to science and botany would be good. I would however like a bold approach to this design - it is a modern brand.

The bottle being used for the product can be seen at: http://www.brevik-flask.example/en/product-groups/8-Apothecary-bottles - these are extremely expensive bottles and the label needs to reflect this quality. These bottles are traditional in design, but incorporate high end glassware technology to preserve the integrity of the natural ingredients. Therefore the product is a mix of old and new, and the label could also reflect this. The colour of the glass is very deep purple.

The front label does not need information such as weight/volume - it purely needs a label which will recognise it as the VRE brand, with the product name. I am looking for a high quality label, which is unique. I am happy to print embossed labels and to use foils on my labels.

Please do not be boring! I appreciate I have given a variety of influences, so summarise the requirements are a mix of:

a bold design
contemporary
luxury

The label must include NO slogans.

I am looking to build a relationship with a graphic designer for packaging and website design requirements so this will be the first of many projects.

Target Market(s)

Luxury end of market - clientele will like luxury and will pay for the highest quality ingredients in the product, but will also appreciate the botanical nature of the product.

Industry/Entity Type

Graphic Designer

Requirements
Must have
• Must include the company name, VRE, although this doesn't need to be particularly prominent. And the product name, e.g. Sandalwood.
Nice to have
• It should combine luxury, but with recognition of the science behind the product.
Should not have
• No slogans, minimal wording on the front label. No other wording other than company name and product name. No primary colours.

```html
<!DOCTYPE html>
<html lang="en">
<head>
<meta charset="utf-8">
<title>VRE Foam Bath Labels</title>
<link rel="stylesheet" href="https://fonts.googleapis.com/css2?family=Pathway+Gothic+One&family=Roboto+Condensed:wght@400;700&display=swap">
<style>
  :root {
    --backdrop: #2b2c30;
    --label-ink: #13131d;
    --label-text: #f2f2f4;
    --rule: #8c8c96;
    --gold: #c9a13a;
    --green: #1f9a5a;
    --violet: #7a5aa6;
  }
  * { margin: 0; padding: 0; box-sizing: border-box; }
  html, body {
    width: 1200px;
    height: 1018px;
    overflow: hidden;
    background: var(--backdrop);
  }
  .label-range {
    width: 1200px;
    height: 1018px;
    display: flex;
    align-items: center;
    justify-content: center;
    gap: 48px;
  }
  .label {
    width: 328px;
    height: 440px;
    background: var(--label-ink);
    color: var(--label-text);
    display: flex;
    flex-direction: column;
    align-items: center;
    padding-top: 96px;
  }
  .brand {
    display: flex;
    align-items: center;
    gap: 14px;
    height: 90px;
  }
  .brand-dot {
    width: 26px;
    height: 26px;
    border-radius: 50%;
    background: var(--accent);
  }
  .brand-name {
    font-family: "Roboto Condensed", sans-serif;
    font-weight: 700;
    font-size: 40px;
    letter-spacing: 2px;
    color: var(--label-text);
  }
  .fragrance {
    margin-top: 58px;
    font-family: "Pathway Gothic One", sans-serif;
    font-size: 48px;
    letter-spacing: 1px;
    line-height: 1;
  }
  .rule {
    width: 208px;
    height: 1px;
    background: var(--rule);
    margin-top: 16px;
  }
  .product-type {
    margin-top: 20px;
    font-family: "Roboto Condensed", sans-serif;
    font-size: 17px;
  }
  .label--sandalwood { --accent: var(--gold); }
  .label--vetiver { --accent: var(--green); }
  .label--neroli { --accent: var(--violet); }
</style>
</head>
<body>
  <main class="label-range">
    <section class="label label--sandalwood">
      <div class="brand"><span class="brand-dot"></span><span class="brand-name">VRE</span></div>
      <h2 class="fragrance">Sandalwood</h2>
      <div class="rule"></div>
      <p class="product-type">Foam Bath</p>
    </section>
    <section class="label label--vetiver">
      <div class="brand"><span class="brand-dot"></span><span class="brand-name">VRE</span></div>
      <h2 class="fragrance">Vetiver</h2>
      <div class="rule"></div>
      <p class="product-type">Foam Bath</p>
    </section>
    <section class="label label--neroli">
      <div class="brand"><span class="brand-dot"></span><span class="brand-name">VRE</span></div>
      <h2 class="fragrance">Neroli</h2>
      <div class="rule"></div>
      <p class="product-type">Foam Bath</p>
    </section>
  </main>
</body>
</html>
```